Need a Modern WIX Website design

Need help designing a modern WIX website. I already started building on editor.wix.com but I am not a designer and would like a more modern, update aesthetic look. This is not an e-commerce site. Just a website portraying our company, posting what products we offer, contact, about us, services. Logo is already on the editor.wix version with some content. Need a designer with vision, and ingenuity to set it apart change it a little and make it stand out. Please look at the current site for redesign and/or ideas https://corvadetradewks.sitebuildr.net/website
also need the design to be connected to our google domain www.ctw.supply

Please feel free to ask as many questions as possible

Target Market(s)

Tire repair shops, Tire stores, mechanic shops, tire replacement franchises, wheel and rim stores

Industry/Entity Type

we are wholesalers, B2B ..sell tire repair materials, tire hand tools, machinery, chemicals, wheel lug nuts, wheel accessories

Coding

Coded - Design and coding required

Number of Pages Required

5+ page

Font styles to use
Other font styles liked:
• Let designer choose

Colors

Designer to choose colors to be used in the design.

Requirements
Must have
• modern design layout, videos, high quality pictures, different ideas for pages (Home, shop, about, products, services, contact, faq, meet the team) translatable english to spanish
Nice to have
• would like to have an up to date modern look, interactive, easy to navigate,
Should not have
• not be hard to navigate for our customers

```html
<!DOCTYPE html>
<html lang="en">
<head>
<meta charset="utf-8">
<title>Corvade Trade Works Inc</title>
<link href="https://fonts.googleapis.com/css2?family=Roboto:wght@300;400;500;700;900&display=swap" rel="stylesheet">
<style>
:root{
  --black:#0b0b0b;
  --ink:#141414;
  --panel:#262626;
  --panel-2:#2e2e2e;
  --red:#d3201f;
  --red-deep:#8e1514;
  --white:#ffffff;
  --soft:#cfcfcf;
  --muted:#a8a8a8;
}
*{box-sizing:border-box;margin:0;padding:0}
html,body{width:1200px;height:5315px;overflow:hidden}
body{background:var(--ink);color:var(--white);font-family:'Roboto',Arial,sans-serif;font-weight:300;position:relative}
.abs{position:absolute}
a{color:inherit;text-decoration:none}

/* header */
.site-header{left:0;top:0;width:1200px;height:110px;z-index:3}
.brand{left:102px;top:38px;display:flex;align-items:center;gap:8px}
.brand-mark{width:30px;height:30px;background:var(--red)}
.brand-name{font-size:24px;font-weight:700;letter-spacing:.5px;color:var(--white)}
.top-tools{right:118px;top:26px;display:flex;gap:40px;font-size:13px;align-items:center}
.main-nav{right:104px;top:66px;display:flex;gap:20px;font-size:13px;font-weight:400}

/* hero */
.hero{left:0;top:0;width:1200px;height:650px;background:var(--black)}
.hero-photo{left:300px;top:130px;width:900px;height:520px;background:radial-gradient(ellipse at 60% 35%,#4a4a4a 0%,#262626 35%,#0b0b0b 72%)}
.hero-title{left:100px;top:200px;font-size:56px;line-height:64px;font-weight:300}
.hero-sub{left:104px;top:344px;font-size:26px;line-height:33px;font-weight:300}
.btn-shop{left:104px;top:440px;width:142px;height:40px;border-radius:20px;background:var(--red);font-size:14px;font-weight:500;display:flex;align-items:center;justify-content:center}
.play{left:574px;top:344px}

/* about */
.about-band{left:0;top:748px;width:1200px;height:352px;background:linear-gradient(90deg,#1c1c1c,#3a3a3a 60%,#2b2b2b)}
.about-red{left:0;top:748px;width:513px;height:352px;background:linear-gradient(135deg,#e12a27,#9e1412)}
.about-photo{left:96px;top:668px;width:380px;height:456px;background:linear-gradient(160deg,#3a3f4b,#1d2b48 45%,#222 100%);border-radius:4px}
.about-copy{left:620px;top:812px;width:432px;font-size:15px;line-height:23px;color:var(--soft)}

/* products */
.section-title{font-size:30px;font-weight:300}
.featured-title{left:93px;top:1207px}
.shop-all{left:1034px;top:1222px;font-size:15px}
.product{width:196px}
.product-img{height:140px;width:140px;margin:0 auto;background:radial-gradient(circle,#d6d6d6,#8a8a8a 60%,transparent 70%)}
.product-name{margin-top:52px;height:68px;font-size:15px;line-height:20px;font-weight:400}
.btn-cart{display:flex;align-items:center;justify-content:center;height:38px;border:1px solid var(--white);font-size:14px}
.arrow{top:1425px}

/* brands */
.brands{left:0;top:1695px;width:1200px;height:585px;background:linear-gradient(90deg,#050505 30%,#1e1e1e 70%,#3a3a3a)}
.brands-title{left:0;width:1200px;text-align:center;top:1755px}
.brands-sub{left:0;width:1200px;text-align:center;top:1805px;font-size:19px;color:var(--soft)}
.brand-tile{width:198px;height:163px;background:var(--panel);border-radius:4px;display:flex;align-items:center;justify-content:center;font-size:26px;font-weight:700}

/* services */
.services-title{left:0;width:1200px;text-align:center;top:2333px;font-size:32px}
.svc-photo{left:588px;width:612px}
.svc-head{font-size:31px;font-weight:300}
.svc-copy{font-size:13.5px;line-height:21px;color:var(--soft)}
.quality-band{left:0;top:2942px;width:1200px;height:363px;background:linear-gradient(90deg,#1a1a1a 20%,#a81a18 55%,#5c1010 100%)}
.quality-photo{left:165px;top:2866px;width:371px;height:434px;border-radius:50%;background:radial-gradient(circle,#8a8a8a 0%,#3a3a3a 35%,#151515 60%,#0d0d0d 70%)}

/* why */
.why-title{left:0;width:1200px;text-align:center;top:3889px;font-size:32px}
.why-card{width:320px;background:var(--panel);text-align:center;padding:0 40px}
.why-card.accent{background:linear-gradient(180deg,#c01d1c,#8d1412)}
.why-card svg{display:block;margin:0 auto}
.why-card h3{font-size:28px;font-weight:300;margin-top:20px}
.why-card p{font-size:14px;line-height:22px;color:var(--soft);margin-top:12px}
.why-card.accent p{color:#f1dada}

/* contact */
.contact-title{left:104px;top:4796px}
.contact-info{left:104px;top:4866px;font-size:15px;line-height:22px;color:var(--soft)}
.contact-info .mail{text-decoration:underline}
.contact-info .phone{margin-top:22px;display:block}
.map{left:454px;top:4759px;width:746px;height:285px;background:linear-gradient(135deg,#3a3a3a,#262626 50%,#333)}

/* footer */
.site-footer{left:0;top:5100px;width:1200px;height:215px;background:linear-gradient(180deg,var(--ink),#4a0c0c)}
.footer-nav{left:0;width:1200px;top:5160px;display:flex;justify-content:center;gap:24px;font-size:13px;font-weight:400}
.socials{left:0;width:1200px;top:5208px;display:flex;justify-content:center;gap:14px}
.socials span{width:20px;height:20px;border-radius:50%;background:var(--white)}
.copyright{left:0;width:1200px;top:5256px;text-align:center;font-size:11px}
</style>
</head>
<body>

<section class="hero abs">
  <div class="hero-photo abs" role="img" aria-label="Close-up of a black tire tread lit from above"></div>
  <h1 class="hero-title abs">Corvade Trade<br>Works Inc</h1>
  <p class="hero-sub abs">Your One Stop Tire Repair<br>Supplier in New York</p>
  <a class="btn-shop abs" href="#">SHOP NOW</a>
  <svg class="play abs" width="52" height="52" viewBox="0 0 52 52" aria-label="Play video"><circle cx="26" cy="26" r="23" fill="none" stroke="#fff" stroke-width="3"/><path d="M20 15 L37 26 L20 37 Z" fill="none" stroke="#fff" stroke-width="3" stroke-linejoin="round"/></svg>
</section>

<header class="site-header abs">
  <div class="brand abs"><span class="brand-mark"></span><span class="brand-name">CORVADE</span></div>
  <div class="top-tools abs">
    <span style="display:flex;align-items:center;gap:8px">Search
      <svg width="14" height="14" viewBox="0 0 14 14"><circle cx="6" cy="6" r="4.5" fill="none" stroke="#fff" stroke-width="1.5"/><path d="M9.5 9.5 L13 13" stroke="#fff" stroke-width="1.5"/></svg></span>
    <span>Log in</span>
    <svg width="18" height="18" viewBox="0 0 18 18"><path d="M3 5 H15 V16 H3 Z M6 5 V3 H12 V5" fill="none" stroke="#fff" stroke-width="1.4"/></svg>
  </div>
  <nav class="main-nav abs">
    <a>Home</a><a>Shop</a><a>About</a><a>Products</a><a>Services</a><a>Contact</a><a>FAQ</a><a>Meet the Team</a><a>Wheel Lug Nuts &amp; Bolts</a>
  </nav>
</header>

<section>
  <div class="about-band abs"></div>
  <div class="about-red abs"></div>
  <div class="about-photo abs" role="img" aria-label="Mechanic in blue overalls rolling a tire next to a chrome alloy wheel"></div>
  <p class="about-copy abs">At Corvade Trade Works Inc we make sure to offer our clients the best selection of tire repair products, tools and machinery as well as provide them with superb customer service. Our staff works with our customers to find exactly the right part they need for the right price. We're here to help inform you about our products, so that you only buy what is absolutely necessary for your establishment. Contact us today to learn more about what we do.</p>
</section>

<section>
  <h2 class="section-title featured-title abs">Featured Products</h2>
  <a class="shop-all abs">Shop all</a>
  <svg class="arrow abs" style="left:102px" width="14" height="22" viewBox="0 0 14 22"><path d="M11 2 L3 11 L11 20" fill="none" stroke="#fff" stroke-width="2"/></svg>
  <svg class="arrow abs" style="left:1084px" width="14" height="22" viewBox="0 0 14 22"><path d="M3 2 L11 11 L3 20" fill="none" stroke="#fff" stroke-width="2"/></svg>
  <div class="product abs" style="left:142px;top:1320px">
    <div class="product-img" role="img" aria-label="Chrome lug nut"></div>
    <p class="product-name">Factory Style - Lug - Trailmark (7/8) M14 1.5</p>
    <a class="btn-cart">add to cart</a>
  </div>
  <div class="product abs" style="left:381px;top:1320px">
    <div class="product-img" role="img" aria-label="Tin of cold vulcanizing fluid" style="background:radial-gradient(circle,#f1f1f1,#bcbcbc 55%,transparent 70%)"></div>
    <p class="product-name">CV-20 COLD VULCANIZING FLUID (FLAMMABLE)</p>
    <a class="btn-cart">add to cart</a>
  </div>
  <div class="product abs" style="left:620px;top:1320px">
    <div class="product-img" role="img" aria-label="Chrome lug nut"></div>
    <p class="product-name">Factory Style - Lug - Trailmark (7/8) M14 1.5</p>
    <a class="btn-cart">add to cart</a>
  </div>
  <div class="product abs" style="left:860px;top:1320px">
    <div class="product-img" role="img" aria-label="Spline lug nut adapter" style="height:40px;width:150px;margin-top:50px;margin-bottom:50px;background:linear-gradient(180deg,#e0e0e0,#7a7a7a)"></div>
    <p class="product-name">Spline Lug Nut - Adapter - Truck Spline w/ 7/8 &amp; 13/16 Drives (7 Spline)</p>
    <a class="btn-cart">add to cart</a>
  </div>
</section>

<section>
  <div class="brands abs" role="img" aria-label="Dark tire tread texture background"></div>
  <h2 class="section-title brands-title abs">Brands</h2>
  <p class="brands-sub abs">Who We Work With</p>
  <div class="brand-tile abs" style="left:165px;top:1882px;color:var(--red)">Ferrox</div>
  <div class="brand-tile abs" style="left:388px;top:1882px;color:#d8d8d8;font-weight:300">Gradient 12</div>
  <div class="brand-tile abs" style="left:612px;top:1882px;color:var(--red);font-size:22px">Halvorn Industries</div>
  <div class="brand-tile abs" style="left:837px;top:1882px;color:var(--white);font-size:24px">Pellwick Tools</div>
  <div class="brand-tile abs" style="left:165px;top:2066px;color:var(--red);font-size:30px">Brindle</div>
  <div class="brand-tile abs" style="left:388px;top:2066px;color:#2f56c9">Quillmark</div>
  <div class="brand-tile abs" style="left:612px;top:2066px;color:#e6c21f;font-size:22px">Northfold Patch</div>
  <div class="brand-tile abs" style="left:837px;top:2066px;color:var(--white);font-weight:900">TESSOR</div>
</section>

<section>
  <h2 class="services-title abs">Services Offered</h2>

  <div class="svc-photo abs" style="top:2443px;height:427px;background:linear-gradient(90deg,#1a1a1a,#4b5360 45%,#6e7684)" role="img" aria-label="Technician kneeling beside a tire in a workshop"></div>
  <h3 class="svc-head abs" style="left:104px;top:2480px">Stellar Customer Service</h3>
  <div class="svc-copy abs" style="left:104px;top:2560px;width:405px">
    <p>For over 25 years, we have been providing excellent customer service by going the extra mile in making sure a customer is happy and satisfied with our company's products or services. We take pride in providing service to a customer in a timely, pleasant manner. In our continuous goal to provide excellent customer service, we have incorporated superb communication and problem resolution skills.</p>
    <p style="margin-top:21px">We offer more than products and tools here at Corvade Trade Works Inc, making sure our clients receive the best services available in the market.</p>
  </div>

  <div class="quality-band abs"></div>
  <div class="quality-photo abs" role="img" aria-label="Tire mounted on a silver multi-spoke alloy wheel"></div>
  <h3 class="svc-head abs" style="left:685px;top:3025px">High Quality Products</h3>
  <p class="svc-copy abs" style="left:685px;top:3095px;width:400px;color:#f0dada">Our products are trusted for their design &amp; engineering, &amp; we will continue to equip our customers with high-quality products and tools at the best value</p>

  <div class="svc-photo abs" style="top:3350px;height:423px;background:linear-gradient(90deg,#1a1a1a,#5a5a5a 45%,#9a9a9a)" role="img" aria-label="Smiling mechanic giving a thumbs up beside a tire"></div>
  <h3 class="svc-head abs" style="left:104px;top:3412px">Commitment</h3>
  <p class="svc-copy abs" style="left:104px;top:3486px;width:405px">When a customer comes to us for parts it is often in the context of a long project. We offer Tire Alignment services that will help guide you throughout the course of your automobile restoration and will save you time and money. This is what differentiates us from other vehicle part replacement stores. Come in and see what we've got to offer you.</p>
</section>

<section>
  <h2 class="why-title abs">Why Choose Us</h2>

  <div class="why-card abs" style="left:105px;top:3969px;height:330px;padding-top:40px">
    <svg width="70" height="50" viewBox="0 0 70 50"><path d="M5 20 L22 8 L35 16 L48 8 L65 20 L45 40 L35 32 L25 40 Z" fill="var(--red)"/></svg>
    <h3>Commitment</h3>
    <p>We understand, respect and value our customers, taking an interest and the time to listen. Open and honest, we keep customers informed about what matters to them.</p>
  </div>
  <div class="why-card accent abs" style="left:439px;top:3969px;height:330px;padding-top:40px">
    <svg width="50" height="50" viewBox="0 0 50 50"><circle cx="25" cy="21" r="12" fill="none" stroke="#ff6a5a" stroke-width="3"/><path d="M19 36 H31 M21 42 H29" stroke="#ff6a5a" stroke-width="3"/></svg>
    <h3>Innovation</h3>
    <p>We keep innovating to improve the experience for customers and everyone who uses our spaces. We are open-minded to new ways of doing things and are keen to hear our customers feedback, always striving to do better.</p>
  </div>
  <div class="why-card abs" style="left:773px;top:3969px;height:330px;padding-top:40px">
    <svg width="60" height="50" viewBox="0 0 60 50"><rect x="8" y="14" width="22" height="22" fill="none" stroke="var(--red)" stroke-width="3" transform="rotate(-20 19 25)"/><rect x="32" y="6" width="16" height="16" fill="var(--red)" transform="rotate(15 40 14)"/></svg>
    <h3>Simplicity</h3>
    <p style="margin-top:20px">We get things done simply and flexibly. We remove unnecessary obstacles so that we are easy for our customers to deal with.</p>
  </div>

  <div class="why-card abs" style="left:272px;top:4351px;height:313px;padding-top:36px">
    <svg width="60" height="50" viewBox="0 0 60 50"><path d="M12 8 H48 L58 20 L30 46 L2 20 Z M2 20 H58 M22 8 L18 20 L30 46 L42 20 L38 8" fill="none" stroke="var(--red)" stroke-width="2.5" stroke-linejoin="round"/></svg>
    <h3>Excellence</h3>
    <p>We achieve high quality in everything we do, committing to excellence in how we do business. Highly professional, we offer exemplary customer service.</p>
  </div>
  <div class="why-card abs" style="left:606px;top:4351px;height:313px;padding-top:36px">
    <svg width="50" height="50" viewBox="0 0 50 50"><circle cx="25" cy="12" r="7" fill="var(--red)"/><path d="M10 46 L14 26 H36 L40 46 Z" fill="var(--red)"/></svg>
    <h3>Proactivity</h3>
    <p>We resolve problems as quick as possible and can be trusted to do as we say. We take responsibility to put things right, collaborating with our partners to drive a swift resolution.</p>
  </div>
</section>

<section>
  <h2 class="section-title contact-title abs">Contact Us</h2>
  <div class="contact-info abs">
    <p>214 Larkmoor Avenue<br>Brookhaven, NY 11719</p>
    <a class="mail">hello@ctw.supply</a>
    <span class="phone">555-014-2290</span>
  </div>
  <div class="map abs" role="img" aria-label="Street map with a pin marking the warehouse location"></div>
</section>

<footer class="site-footer abs"></footer>
<nav class="footer-nav abs">
  <a>Home</a><a>Shop</a><a>About</a><a>Products</a><a>Services</a><a>Contact</a><a>FAQ</a><a>Meet the Team</a><a>Wheel Lug Nuts &amp; Bolts</a>
</nav>
<div class="socials abs" aria-label="Social links"><span></span><span></span><span></span></div>
<p class="copyright abs">©2022 by Corvade Trade Works Inc. Proudly</p>

</body>
</html>
```